Wine label design for my wife. Wine called "The Mirabel"

I need a wine label face lift of one of my premium wines in my collection. My wine sells in Harbor Lark's all over the States. My current label is called The Mirabel (my wife's name) and the illustration of her eyes is done by a well know artist from South Africa. I do not have to use this illustration and therefor I attached several pictures of her and her eyes, even when she was a little girl. The wine's also made in South Africa. This is a premium wine that we only sell 2000 bottles per year. The wine sells at 60 usd per bottle, The current label is too white. I also think her eyes should look more at the person buying it, than away from them.

Target Market(s)

Top end wine buyers

Font styles to use
Decorative
Script

Requirements
Must have
• 'The Mirabel' must be on the label
An illustration must be on the label
Basically all the info that's on the current label must be on by law. As per Sample
Nice to have
• Maybe some ideas of her whole face?
Should not have
• any gold colour

```html
<!DOCTYPE html>
<html lang="en">
<head>
<meta charset="utf-8">
<title>The Mirabel – Sauvignon Blanc 2017</title>
<link rel="stylesheet" href="https://fonts.googleapis.com/css2?family=Crimson+Pro:wght@500;700&family=Italianno&display=swap">
<style>
  :root {
    --label-top: #1d3f48;
    --label-mid: #3b3338;
    --label-bottom: #560f18;
    --panel-navy: #0f1221;
    --panel-teal: #2a4a55;
    --panel-wine: #5a1a26;
    --ink-white: #ffffff;
    --ink-shadow: rgba(8, 10, 24, 0.85);
  }

  * { margin: 0; padding: 0; box-sizing: border-box; }

  html, body {
    width: 1200px;
    height: 668px;
    overflow: hidden;
    background: var(--panel-navy);
  }

  .wine-label {
    position: relative;
    width: 1200px;
    height: 668px;
    overflow: hidden;
    background: linear-gradient(180deg, var(--label-top) 0%, var(--label-mid) 50%, var(--label-bottom) 100%);
    color: var(--ink-white);
  }

  .portrait-panel {
    position: absolute;
    top: 0;
    left: 949px;
    width: 251px;
    height: 668px;
    background: var(--panel-navy);
  }

  .portrait-art {
    position: absolute;
    top: 0;
    left: 838px;
    width: 362px;
    height: 668px;
  }

  .winery-name,
  .varietal,
  .vintage {
    position: absolute;
    left: 270px;
    width: 670px;
    font-family: "Crimson Pro", Georgia, serif;
    line-height: 1;
    text-align: center;
    color: var(--ink-white);
    white-space: nowrap;
  }

  .winery-name {
    top: 4px;
    font-size: 58px;
    font-weight: 700;
    letter-spacing: 1px;
  }

  .wine-name {
    position: absolute;
    top: 263px;
    left: 270px;
    width: 670px;
    font-family: "Italianno", cursive;
    font-size: 180px;
    font-weight: 400;
    line-height: 1;
    text-align: center;
    color: var(--ink-white);
    white-space: nowrap;
  }

  .name-rule {
    position: absolute;
    top: 436px;
    left: 314px;
    width: 572px;
    height: 3px;
    background: linear-gradient(90deg, rgba(255,255,255,0.4), var(--ink-white) 12%, var(--ink-white) 88%, rgba(255,255,255,0.4));
  }

  .varietal,
  .vintage {
    font-size: 58px;
    font-weight: 500;
    text-shadow: 2px 2px 0 var(--ink-shadow);
  }

  .varietal {
    top: 460px;
    letter-spacing: 1.5px;
  }

  .vintage {
    top: 529px;
  }
</style>
</head>
<body>
  <main class="wine-label">
    <div class="portrait-panel"></div>
    <svg class="portrait-art" viewBox="0 0 362 668" role="img" aria-label="Line-art profile illustration of a woman, rendered in flowing teal and wine-red contour lines">
      <defs>
        <linearGradient id="portrait-tone" x1="0" y1="0" x2="0" y2="1">
          <stop offset="0%" stop-color="#2a4a55" stop-opacity="0.55"/>
          <stop offset="55%" stop-color="#0f1221" stop-opacity="0.9"/>
          <stop offset="100%" stop-color="#5a1a26" stop-opacity="0.6"/>
        </linearGradient>
      </defs>
      <path d="M362 0 L362 668 L300 668 C250 560 170 470 110 430 C80 400 70 360 80 320 C100 260 150 210 230 150 C290 100 330 50 362 0 Z" fill="url(#portrait-tone)"/>
    </svg>

    <h2 class="winery-name">HALCYON RIDGE WINES</h2>
    <h1 class="wine-name">The Mirabel</h1>
    <div class="name-rule"></div>
    <p class="varietal">SAUVIGNON BLANC</p>
    <p class="vintage">2017</p>
  </main>
</body>
</html>
```